"Global Leadership & Talent Development Firm" needs a website upgrade

Website Design Project is intended to find a vendor to update and provide maintenance for my website: www.Brightpath7Gains.com. I am looking for a vendor who is an expert with WordPress and eCommerce plugin.

Website Requirements
www.Brightpath7Gains.com

• Media Library (review)- Add video/utube
• Others (plug-ins)
1) eCommerce ability
a) Must have the ability to charge for the eLearning courses
i) Handle credit card processing
ii) Ability to handle yearly subscriptions
iii) Ability to process credits/refunds

Website Updates Assessment Page:
• Totally MORV- Distributor Information
• 4 Crew Patterns Assessment & logo
• Steering Quest- 360 Assessment
• Emotional Intelligence Assessment
Home & Tool Pages:
• K7V License and certification
• PulseCore Trainer
• 4 Crew Patterns training
Client & Contact Pages
• Update Client list
• Update testimonials
Speaker Page Update
Website Add on E-Commerce to sell products
• K7V Certification Program
• PulseCore tools & technology
• Totally MoRV Assessment Distributor
• 4 Crew Pattern Distributor

See attached document describing the updates.

Target Market(s)

Small-Large Business and Corporations
Public Sector Organizations

Industry/Entity Type

Leadership

Number of Pages Required

5+ page

Font styles to use
Other font styles liked:
• www.brightpath7gains.com

Requirements
Must have
• Wordpress expertise
• E-Commerce plugin expertise
• Website Maintenance capability
Nice to have
• Easy access to transfer documents and get feedback/suggestions on the best wording for presenting the information onto my site for each of the pages
Should not have
• Focus on changing the current design of my site

```html
<!DOCTYPE html>
<html lang="en">
<head>
<meta charset="utf-8">
<title>Brightpath7Gains – Leadership & Talent Development</title>
<link href="https://fonts.googleapis.com/css2?family=Montserrat:wght@400;500;600;700&display=swap" rel="stylesheet">
<style>
:root{
  --orange:#f0961e;
  --orange-dark:#e2871a;
  --ink:#4a4a4a;
  --muted:#8a8a8a;
  --light:#f4f4f4;
  --white:#ffffff;
  --hero-dark:#2b2320;
  --map-dark:#4a4b4d;
  --footer:#8c8c8c;
}
*{box-sizing:border-box;margin:0;padding:0}
html,body{width:671px;height:1200px;overflow:hidden}
body{position:relative;font-family:'Montserrat',Arial,sans-serif;color:var(--ink);background:var(--white)}
.abs{position:absolute}

/* hero */
.hero{left:0;top:0;width:671px;height:378px;
  background:radial-gradient(ellipse at 40% 45%,#7a5a3c 0%,#4a3628 45%,var(--hero-dark) 100%)}
.hero-photo{position:absolute;inset:0;background:linear-gradient(90deg,rgba(160,120,80,.35),rgba(60,45,35,.1) 50%,rgba(120,90,60,.3))}
.navbar{left:52px;top:22px;width:567px;height:30px;background:var(--white);border-radius:4px;box-shadow:0 1px 3px rgba(0,0,0,.3);display:flex;align-items:center}
.brand{display:flex;align-items:center;gap:4px;margin-left:9px;width:100px}
.brand-mark{width:13px;height:13px;background:var(--orange);border-radius:2px}
.brand-name{font-size:8px;font-weight:500;color:var(--ink);letter-spacing:-.2px}
.nav{display:flex;gap:0;margin-left:12px;font-size:6.2px;color:var(--ink);list-style:none}
.nav li{white-space:nowrap}
.nav li+li::before{content:"/";margin:0 5px;color:var(--muted)}
.nav .active{color:var(--orange);position:relative}
.nav .active::after{content:"";position:absolute;left:0;right:0;top:14px;height:2px;background:var(--orange)}
.hero-title{left:0;top:146px;width:671px;text-align:center;color:var(--white);font-weight:700;font-size:21px;line-height:25px}
.hero-title em{font-style:normal;color:var(--orange)}
.hero-copy{left:200px;top:204px;width:271px;text-align:center;color:#d8d0c8;font-size:5.6px;line-height:7.2px}
.btn-outline{left:302px;top:237px;width:67px;height:21px;border:1px solid var(--orange);border-radius:3px;color:var(--orange);font-size:7.5px;font-weight:500;display:flex;align-items:center;justify-content:center}

/* tools */
.tools{left:0;top:378px;width:671px;height:163px;background:var(--light)}
.section-title{width:671px;left:0;text-align:center;color:var(--orange);font-size:13px;font-weight:600}
.tool{width:94px;height:94px;border-radius:50%;background:var(--white);text-align:center}
.tool.is-active{border:1.5px solid var(--orange)}
.tool-icon{position:absolute;left:29px;top:-15px;width:35px;height:35px;border-radius:50%;background:#ececec;display:flex;align-items:center;justify-content:center}
.tool.is-active .tool-icon{background:var(--orange)}
.tool-name{position:absolute;left:6px;width:82px;top:30px;font-size:6px;font-weight:600;color:var(--ink)}
.tool.is-active .tool-name{color:var(--orange)}
.tool-text{position:absolute;left:12px;width:70px;top:40px;font-size:4.8px;line-height:6px;color:var(--muted)}
.tool-more{position:absolute;left:0;width:92px;top:59px;font-size:5px;color:var(--orange)}
.tool-go{position:absolute;left:41px;top:69px;width:10px;height:10px;border-radius:50%;background:#eee;display:flex;align-items:center;justify-content:center}
.tool.is-active .tool-go{background:#666}

/* approach */
.approach{left:0;top:541px;width:671px;height:329px;
  background:linear-gradient(90deg,#8a6a7a 0%,#e8d8d0 35%,#f4ece6 50%,#e6d4c6 65%,#9a6a50 100%)}
.approach-copy{left:205px;top:590px;width:261px;text-align:center;font-size:5.2px;line-height:7.8px;color:#4a4040}
.approach-copy span{color:var(--orange)}
.video{left:167px;top:641px;width:337px;height:190px;border:1.5px solid var(--orange);background:linear-gradient(180deg,#4e4a44 0%,#3a3632 60%,#2a2826 100%);overflow:hidden}
.play{left:154px;top:82px;width:30px;height:30px;border:1.5px solid rgba(255,255,255,.75);border-radius:50%}
.controls{left:0;bottom:0;width:100%;height:16px;background:rgba(0,0,0,.55)}
.timecode{left:70px;top:5px;font-size:5px;color:#ddd}

/* contact */
.contact{left:0;top:870px;width:671px;height:144px;background:var(--light)}
.contact-info{left:95px;top:913px;width:160px;font-size:5px;line-height:8px;color:var(--muted)}
.contact-info h4{font-size:6px;color:var(--ink);font-weight:600;margin-top:3px;line-height:8px}
.contact-info .link{color:var(--orange)}
.field{width:130px;height:18px;border:1px solid var(--orange);border-radius:4px;background:var(--white);font-size:6px;color:var(--muted);padding:5px 6px}
.btn-submit{left:307px;top:979px;width:60px;height:18px;background:var(--orange);border-radius:3px;color:var(--white);font-size:6px;font-weight:600;display:flex;align-items:center;justify-content:center}

/* map & footer */
.map{left:0;top:1014px;width:671px;height:161px;background:linear-gradient(135deg,#545556,#434446 60%,#4c4d50)}
.footer{left:0;top:1175px;width:671px;height:25px;background:var(--footer);color:var(--white);font-size:6px;display:flex;align-items:center;justify-content:center;gap:6px}
.footer .link{color:var(--orange)}
</style>
</head>
<body>

<section class="abs hero">
  <div class="hero-photo" role="img" aria-label="Photo of a business team meeting around a table, warm tone"></div>
</section>

<header class="abs navbar">
  <div class="brand"><span class="brand-mark"></span><span class="brand-name">Brightpath7Gains</span></div>
  <ul class="nav">
    <li class="active">Home</li><li>Approach</li><li>Tools</li><li>Assessments</li><li>Clients</li><li>Consultants</li><li>Speaking</li><li>Blog</li><li>Contact B7G</li><li>E-Commerce</li>
  </ul>
</header>

<h1 class="abs hero-title">Behind every <em>good result</em><br>is a <em>great insight.</em></h1>
<p class="abs hero-copy">Neque porro quisquam est qui dolorem ipsum quia dolor sit amet, consectetur, adipisci velit..Neque porro quisquam est qui dolorem ipsum quia dolor sit amet, consectetur, adipisci velit..</p>
<div class="abs btn-outline">Learn More</div>

<section class="abs tools"></section>
<h2 class="abs section-title" style="top:389px">Tools</h2>

<div class="abs tool is-active" style="left:83px;top:433px">
  <div class="tool-icon"><svg width="16" height="14" viewBox="0 0 16 14"><g stroke="#fff" stroke-width="1.3" fill="none"><path d="M1 13h14"/><path d="M3 12V8M6 12V6M9 12V7M12 12V4"/><path d="M2 7l4-3 3 2 5-4"/></g></svg></div>
  <div class="tool-name">Coaching7Gains™</div>
  <div class="tool-text">Most leaders believe that setting ambitious goals..</div>
  <div class="tool-more">Read More</div>
  <div class="tool-go"><svg width="4" height="5" viewBox="0 0 4 5"><path d="M1 .5l2 2-2 2" stroke="#fff" fill="none" stroke-width=".8"/></svg></div>
</div>
<div class="abs tool" style="left:220px;top:433px">
  <div class="tool-icon"><svg width="16" height="16" viewBox="0 0 16 16"><g stroke="#777" stroke-width="1.2" fill="none"><circle cx="8" cy="8" r="6"/><circle cx="8" cy="7" r="2"/><path d="M4.5 12c1-2 6-2 7 0"/></g></svg></div>
  <div class="tool-name">Managing7Gains™</div>
  <div class="tool-text">Management training must equip and empower..</div>
  <div class="tool-more">Read More</div>
  <div class="tool-go"><svg width="4" height="5" viewBox="0 0 4 5"><path d="M1 .5l2 2-2 2" stroke="#888" fill="none" stroke-width=".8"/></svg></div>
</div>
<div class="abs tool" style="left:357px;top:433px">
  <div class="tool-icon"><svg width="16" height="16" viewBox="0 0 16 16"><g fill="#777"><circle cx="8" cy="6" r="3.5"/><path d="M2 15c0-4 12-4 12 0z"/></g></svg></div>
  <div class="tool-name">Mentoring7Gains™</div>
  <div class="tool-text">Research shows that employees entering the ..</div>
  <div class="tool-more">Read More</div>
  <div class="tool-go"><svg width="4" height="5" viewBox="0 0 4 5"><path d="M1 .5l2 2-2 2" stroke="#888" fill="none" stroke-width=".8"/></svg></div>
</div>
<div class="abs tool" style="left:494px;top:433px">
  <div class="tool-icon"><svg width="16" height="16" viewBox="0 0 16 16"><g stroke="#777" stroke-width="1.2" fill="none"><path d="M8 3a4 4 0 0 0-2 7.5V12h4v-1.5A4 4 0 0 0 8 3z"/><path d="M6.5 14h3"/></g></svg></div>
  <div class="tool-name" style="top:25px">Core Outlook<br>Gauge®</div>
  <div class="tool-text">Achieving results is about closing gaps and turning..</div>
  <div class="tool-more">Read More</div>
  <div class="tool-go"><svg width="4" height="5" viewBox="0 0 4 5"><path d="M1 .5l2 2-2 2" stroke="#888" fill="none" stroke-width=".8"/></svg></div>
</div>

<section class="abs approach" role="img" aria-label="Photo of two women talking at a sunlit table"></section>
<h2 class="abs section-title" style="top:557px">Our Approach</h2>
<p class="abs approach-copy">Looking for a boxed approach? You won't find it here. Our approach is an exchange; an exchange of dynamic listening and deliberate question asking. We ultimately identify the key leadership and talent factors that influence your organization's issues and successes.<br><span>Read More</span></p>

<div class="abs video" role="img" aria-label="Video still of a consultant speaking on a city street">
  <div class="abs play"><svg width="27" height="27" viewBox="0 0 27 27"><path d="M11 8l8 5.5-8 5.5z" fill="rgba(255,255,255,.8)"/></svg></div>
  <div class="abs controls">
    <svg class="abs" style="left:14px;top:4px" width="50" height="8" viewBox="0 0 50 8"><g fill="#ccc"><path d="M0 0l6 4-6 4z"/><path d="M18 0l5 4-5 4zM23 0l5 4-5 4z"/><rect x="29" y="0" width="1" height="8"/><path d="M38 2h2l3-2v8l-3-2h-2z"/></g></svg>
    <span class="abs timecode">0:38 / 10:18</span>
    <svg class="abs" style="right:12px;top:4px" width="62" height="8" viewBox="0 0 62 8"><g fill="none" stroke="#ccc" stroke-width="1"><rect x="1" y="1" width="8" height="6"/><circle cx="22" cy="4" r="3"/><rect x="34" y="1" width="9" height="6"/><path d="M52 3V1h2M59 1h2v2M61 5v2h-2M54 7h-2V5"/></g></svg>
  </div>
</div>

<section class="abs contact"></section>
<h2 class="abs section-title" style="top:879px">Contact Us</h2>
<div class="abs contact-info">
  <p>To enquire about a leadership expedition or for specific information on how we can serve an organization like yours, please contact us.</p>
  <h4>Email:</h4>
  <p class="link">dana@brightpath7gains.com</p>
  <h4>To talk to us:</h4>
  <p class="link">555.010-2736</p>
  <p style="margin-top:4px">Or drop your information below and we will contact you.</p>
</div>
<div class="abs field" style="left:307px;top:913px">Full Name</div>
<div class="abs field" style="left:307px;top:934px">E-mail</div>
<div class="abs field" style="left:307px;top:955px">Subject</div>
<div class="abs field" style="left:447px;top:913px;height:60px">Your Comment</div>
<div class="abs btn-submit">Submit</div>

<section class="abs map" role="img" aria-label="Street map of the office neighbourhood"></section>

<footer class="abs footer">
  <span>Copyright 2012 Brightpath7Gains, LLC / All Rights Reserved</span><span>/</span>
  <span class="link">dana@brightpath7gains.com</span><span>/</span>
  <span class="link">(555) 010-2736</span>
</footer>

</body>
</html>
```